Helping Seniors and their families start the discussion about driver safety, and explore options to preserve senior independence.
Target Market(s)
Seniors and their families
Industry/Entity Type
Non Profit
Number of Pages Required
4 page
Font styles to use
Sans Serif
Requirements
Must have
- Logo
- Application for Bright Pathways Registration

Nice to have
- Colorful, and designed for Senior Citizens and their Families

```html
<!DOCTYPE html>
<html lang="en">
<head>
<meta charset="utf-8">
<title>Bright Pathways — Keeping Us Safe</title>
<link href="https://fonts.googleapis.com/css2?family=Montserrat:wght@400;600;700;800&family=Open+Sans:ital,wght@0,400;0,600;0,700;1,700&display=swap" rel="stylesheet">
<style>
:root{
  --green:#0c9b4c;
  --green-dark:#087a3a;
  --ink:#2b2b2b;
  --ink-soft:#555;
  --grey:#8a8a8a;
  --line:#e2e2e2;
  --charcoal:#262626;
  --white:#fff;
  --photo-a:#d9d6d1;
  --photo-b:#b9b4ad;
}
*{box-sizing:border-box;margin:0;padding:0}
html,body{width:1200px;height:4467px;overflow:hidden}
body{font-family:"Open Sans",Arial,sans-serif;color:var(--ink);background:var(--white);font-size:12px;line-height:1.6}
h1,h2,h3,h4,.nav,.btn{font-family:"Montserrat",Arial,sans-serif}
.wrap{width:704px;margin:0 auto;position:relative}
section,header,footer{position:relative;overflow:hidden}

/* top bar */
.topbar{height:30px;background:var(--green-dark);color:var(--white);font-size:9px;display:flex;align-items:center;justify-content:space-between;padding:0 252px}
.topbar span{display:flex;align-items:center;gap:5px;white-space:nowrap}
.topbar svg{width:9px;height:9px;fill:var(--white)}

/* header */
.site-header{height:90px;border-bottom:1px solid var(--line)}
.site-header .wrap{height:90px}
.brand{position:absolute;left:0;top:18px;display:flex;align-items:center;gap:8px}
.brand-dot{width:16px;height:16px;border-radius:50%;background:var(--green)}
.brand-name{font-family:"Montserrat",sans-serif;font-weight:800;font-size:24px;line-height:1;color:var(--green)}
.book{position:absolute;right:110px;top:12px;text-align:right;font-size:9px;color:var(--grey);line-height:1.2}
.book b{display:block;color:var(--green);font-family:"Montserrat",sans-serif;font-size:14px}
.socials{position:absolute;right:0;top:16px;display:flex;gap:6px}
.socials i{width:20px;height:20px;border-radius:50%;background:var(--green);display:block}
.nav{position:absolute;right:0;top:60px;display:flex;gap:22px;font-size:11px;font-weight:600;color:var(--ink-soft);align-items:center}
.nav .active{color:var(--green);border-bottom:2px solid var(--green);padding-bottom:4px}
.nav svg{width:12px;height:12px;stroke:var(--ink-soft);fill:none;stroke-width:2}

/* hero */
.hero{height:497px;background:var(--green)}
.hero-photo{position:absolute;left:0;top:0;width:720px;height:497px;background:linear-gradient(135deg,#d8d3cc 0%,#b8b0a6 50%,#9c948a 100%);clip-path:polygon(0 0,100% 0,82% 100%,0 100%)}
.hero-panel{position:absolute;left:560px;top:0;width:640px;height:497px;background:linear-gradient(90deg,#0a8f44,#0c9b4c);clip-path:polygon(28% 0,100% 0,100% 100%,0 100%)}
.hero-copy{position:absolute;left:588px;top:210px;color:var(--white)}
.hero-copy h1{font-size:43px;font-weight:800;line-height:1}
.hero-copy p{font-family:"Montserrat",sans-serif;font-weight:700;font-size:15px;line-height:1.2;margin-top:6px}

/* why */
.why{height:483px}
.why h2{position:absolute;left:0;top:66px;font-size:25px;font-weight:800;color:var(--green);white-space:nowrap}
.why-text{position:absolute;left:0;top:112px;width:308px;font-size:8.5px;line-height:1.55;color:var(--ink-soft)}
.why-text p{margin-bottom:10px}
.btn-outline{position:absolute;left:0;top:395px;width:140px;height:30px;border:1px solid var(--green);color:var(--green);font-size:9px;font-weight:700;display:flex;align-items:center;justify-content:center}
.reg{position:absolute;right:0;top:56px;width:290px;height:380px;background:#333;padding:0 20px}
.reg h3{margin:0 -20px 18px;height:46px;background:var(--green);color:var(--white);font-size:18px;font-weight:800;display:flex;align-items:center;justify-content:center;letter-spacing:.5px}
.reg .field{height:30px;background:var(--white);margin-bottom:12px;font-size:9px;color:#999;padding:0 8px;display:flex;align-items:center}
.reg .submit{height:32px;background:var(--green);color:var(--white);font-family:"Montserrat",sans-serif;font-weight:700;font-size:11px;display:flex;align-items:center;justify-content:center;margin-top:4px}

/* services band */
.services-band{height:216px;background:var(--green);text-align:center;color:var(--white)}
.services-band .ghost{position:absolute;right:0;top:0;width:240px;height:216px;background:linear-gradient(90deg,rgba(12,155,76,0),rgba(150,190,160,.45))}
.services-band h2{position:relative;padding-top:52px;font-size:37px;font-weight:800;line-height:1}
.services-band p{position:relative;width:600px;margin:12px auto 0;font-size:13px;line-height:1.3}

/* service tiles */
.tiles{height:284px}
.tiles .row{position:absolute;left:0;top:62px;display:flex;gap:8px}
.tile{position:relative;width:170px;height:170px}
.tile svg.oct{position:absolute;inset:0;width:170px;height:170px}
.tile .inner{position:absolute;inset:0;padding:34px 22px 0;text-align:center}
.tile .ico{width:22px;height:22px;margin:0 auto 10px;display:block}
.tile h4{font-size:10px;font-weight:700;color:var(--green);line-height:1.2}
.tile p{font-size:8px;color:var(--grey);line-height:1.45;margin-top:4px}
.tile.on h4,.tile.on p{color:var(--white)}

/* participation */
.participation{height:351px;background:#f4f4f4;border-top:1px solid var(--line)}
.participation h2{position:absolute;left:0;top:54px;font-size:23px;font-weight:800;color:var(--green);white-space:nowrap}
.ticks{position:absolute;left:0;top:108px;width:420px;list-style:none}
.ticks li{display:flex;gap:8px;font-size:9px;color:var(--ink-soft);padding:7px 0;border-bottom:1px solid var(--line);line-height:1.4}
.ticks svg{flex:0 0 9px;width:9px;height:9px;margin-top:3px;stroke:var(--green);fill:none;stroke-width:3}
.part-photo{position:absolute;right:-6px;top:60px;width:250px;height:236px;background:linear-gradient(160deg,var(--photo-b),var(--photo-a))}

/* pricing */
.pricing{height:635px;background:linear-gradient(180deg,#2c2c2c,#1e1e1e);color:var(--white);text-align:center}
.pricing .bg{position:absolute;inset:0;background:radial-gradient(ellipse at 85% 70%,rgba(120,120,120,.3),transparent 60%),radial-gradient(ellipse at 10% 30%,rgba(90,90,90,.25),transparent 55%)}
.pricing h2{position:relative;padding-top:52px;font-size:27px;font-weight:800}
.pricing .lead{position:relative;width:580px;margin:4px auto 0;font-size:12.5px;line-height:1.35}
.plans{position:absolute;left:250px;top:210px;display:flex;gap:24px}
.plan{position:relative;width:216px;height:370px;border:1px solid rgba(255,255,255,.35);padding-top:90px}
.plan.featured{background:var(--green);border:6px solid rgba(255,255,255,.25);width:222px;height:378px;margin-top:-4px}
.diamond{position:absolute;left:50%;top:-38px;width:80px;height:80px;margin-left:-40px;transform:rotate(45deg);border:2px solid var(--white);background:#242424;display:flex;align-items:center;justify-content:center}
.plan.featured .diamond{background:var(--green)}
.diamond span{transform:rotate(-45deg);font-family:"Montserrat",sans-serif;font-size:20px;font-weight:700}
.plan h3{font-size:17px;font-weight:800;margin-bottom:14px}
.plan ul{list-style:none;margin:0 12px}
.plan li{font-size:10px;height:29px;display:flex;align-items:center;justify-content:center;border-top:1px solid rgba(255,255,255,.25)}
.plan .join{width:120px;height:28px;margin:12px auto 0;background:var(--white);color:var(--ink);font-size:10px;font-weight:600;display:flex;align-items:center;justify-content:center}
.plan.featured .join{color:var(--green)}

/* testimonials */
.testimonials{height:393px;background:linear-gradient(180deg,#dcdcdc,#efefef 40%,#e4e4e4);text-align:center}
.testimonials h2{padding-top:52px;font-size:27px;font-weight:800;color:var(--ink)}
.avatar{width:100px;height:100px;border-radius:50%;margin:14px auto 0;background:linear-gradient(180deg,#b7c1ca,#7d8b98);border:4px solid var(--white);box-shadow:0 0 0 2px var(--green)}
.testimonials h4{margin-top:10px;font-size:10px;color:var(--green);font-weight:700}
.testimonials .role{font-size:8px;color:var(--grey)}
.quote{position:relative;width:520px;margin:12px auto 0;font-size:10px;line-height:1.5;color:var(--ink-soft)}
.qm{position:absolute;font-family:Georgia,serif;font-size:54px;color:#b9b9b9;line-height:1}
.qm.l{left:-40px;top:-20px}.qm.r{right:-40px;bottom:-40px}
.arrow{position:absolute;top:180px;width:44px;height:44px;background:#3a3a3a;display:flex;align-items:center;justify-content:center}
.arrow svg{width:12px;height:12px;stroke:var(--white);fill:none;stroke-width:2.5}
.arrow.prev{left:0}.arrow.next{right:0}

/* reservation */
.reservation{height:167px;background:var(--green);text-align:center;color:var(--white)}
.reservation h2{padding-top:34px;font-size:30px;font-weight:800;line-height:1}
.reservation p{font-size:10px;width:300px;margin:8px auto 0;line-height:1.4}
.reservation .phone{font-style:italic;font-weight:700;font-size:28px;margin-top:10px;line-height:1}

/* go when */
.gowhen{height:458px}
.gowhen h2{position:absolute;left:0;top:64px;width:400px;font-size:20px;font-weight:800;color:var(--green);line-height:1.15}
.gowhen ul{position:absolute;left:0;top:124px;list-style:none}
.gowhen li{display:flex;gap:7px;align-items:center;font-size:9px;color:var(--ink-soft);height:16px}
.gowhen li svg{width:8px;height:8px;stroke:var(--green);fill:none;stroke-width:3}
.go-photo{position:absolute;right:-6px;top:60px;width:300px;height:360px;background:linear-gradient(160deg,var(--photo-b),var(--photo-a))}

/* faq */
.faq{height:507px}
.faq h2{position:absolute;left:0;right:0;top:60px;text-align:center;font-size:28px;font-weight:800;color:var(--green)}
.faq .lead{position:absolute;left:130px;width:444px;top:100px;text-align:center;font-size:9px;color:var(--ink-soft);line-height:1.45}
.acc{position:absolute;left:0;top:176px;width:360px}
.acc .item{border:1px solid var(--line);margin-bottom:8px;font-size:8.5px;color:var(--ink-soft)}
.acc .q{height:26px;display:flex;align-items:center;padding:0 10px;gap:8px}
.acc .q svg{width:8px;height:8px;stroke:var(--green);fill:none;stroke-width:3}
.acc .item.open .q{background:var(--green);color:var(--white)}
.acc .item.open .q svg{stroke:var(--white)}
.acc .a{padding:8px 12px;line-height:1.5;font-size:8px}
.car{position:absolute;right:-40px;top:170px;width:320px;height:220px;background:linear-gradient(180deg,#f4f4f4,#e4e4e4)}

/* newsletter */
.newsletter{height:148px;background:var(--charcoal);color:var(--white)}
.newsletter .label{position:absolute;left:0;top:48px;font-family:"Montserrat",sans-serif;line-height:1.2}
.newsletter .label small{display:block;font-size:9px;font-weight:700}
.newsletter .label strong{font-size:16px;font-weight:800}
.newsletter .field{position:absolute;left:300px;top:70px;width:404px;border-bottom:1px solid #777;font-size:9px;color:#bbb;padding-bottom:6px}
.newsletter .field svg{position:absolute;right:0;top:0;width:12px;height:12px;fill:var(--white)}

/* footer */
.site-footer{height:179px;background:var(--green);color:var(--white)}
.cols{position:absolute;left:250px;top:36px;display:flex}
.col{width:176px}
.col h4{font-size:13px;font-weight:800;margin-bottom:10px;white-space:nowrap}
.col ul{list-style:none;font-size:8.5px;line-height:1.95}
.col li::before{content:"\203A";margin-right:6px}
.col p{font-size:8px;line-height:1.55;margin-bottom:4px;width:150px}
.post{display:flex;gap:8px;align-items:center;margin-bottom:12px;font-size:8px;line-height:1.3}
.post i{width:34px;height:34px;border-radius:50%;background:#2c2c2c;flex:0 0 34px}
.rings{display:flex;gap:5px;margin-top:6px}
.rings i{width:18px;height:18px;border-radius:50%;border:1px solid var(--white);display:block}
.copy{height:30px;background:#1d1d1d;color:#bbb;font-size:8px;display:flex;align-items:center;padding-left:250px}
</style>
</head>
<body>

<div class="topbar">
  <span><svg viewBox="0 0 10 10"><path d="M5 0a3.5 3.5 0 0 0-3.5 3.5C1.5 6 5 10 5 10s3.5-4 3.5-6.5A3.5 3.5 0 0 0 5 0z"/></svg>Address : 214 Meadowlark Lane, Suite 9, Fairview, CA 90210</span>
  <span><svg viewBox="0 0 10 10"><path d="M2 0l2 2.5-1 1.3a6 6 0 0 0 3.2 3.2L7.5 6 10 8 8.6 10C4 9.6.4 6 0 1.4z"/></svg>Phone Number : 555-318-2046</span>
  <span><svg viewBox="0 0 10 10"><path d="M0 2h10v6H0zM0 2l5 3.5L10 2" stroke="#087a3a" stroke-width=".8"/></svg>E-mail : hello@brightpathways.org</span>
</div>

<header class="site-header">
  <div class="wrap">
    <div class="brand"><span class="brand-dot"></span><span class="brand-name">Bright Pathways</span></div>
    <div class="book">BOOK:<b>555-318-2046</b></div>
    <div class="socials"><i></i><i></i><i></i><i></i></div>
    <nav class="nav">
      <span class="active">HOME</span><span>ABOUT</span><span>SERVICES</span><span>INSTRUCTORS</span><span>BLOG</span><span>CONTACT</span>
      <svg viewBox="0 0 12 12"><circle cx="5" cy="5" r="3.8"/><path d="M8 8l3.5 3.5"/></svg>
    </nav>
  </div>
</header>

<section class="hero">
  <div class="hero-panel"></div>
  <div class="hero-photo" role="img" aria-label="Photo of a smiling senior couple seated in a convertible"></div>
  <div class="hero-copy">
    <h1>KEEPING US SAFE</h1>
    <p>PROVIDING PRACTICAL, REAL LIFE SOLUTIONS<br>TO OLDER DRIVERS AND THEIR FAMILIES</p>
  </div>
</section>

<section class="why">
  <div class="wrap">
    <h2>WHY BRIGHT PATHWAYS?</h2>
    <div class="why-text">
      <p>Convenience with our program means you can schedule a ride at a time that suits you, without depending on others and without giving up the routines you enjoy. Our team plans each trip around your needs, from medical visits to weekly errands, so every outing is calm and on time.</p>
      <p>Convenience with our program means you can schedule a ride at a time that suits you, without depending on others and without giving up the routines you enjoy. Our team plans each trip around your needs, from medical visits to weekly errands, so every outing is calm and on time.</p>
      <p>Convenience with our program means you can schedule a ride at a time that suits you, without depending on others and without giving up the routines you enjoy. Our team plans each trip around your needs, from medical visits to weekly errands, so every outing is calm and on time.</p>
      <p>Convenience with our program means you can schedule a ride at a time that suits you, without depending on others and without giving up the routines you enjoy. Our team plans each trip around your needs, from medical visits to weekly errands, so every outing is calm and on time.</p>
    </div>
    <span class="btn btn-outline">READ MORE</span>

    <form class="reg">
      <h3>REGISTRATION CHAPTER</h3>
      <div class="field">Register as</div>
      <div class="field">Enter Name</div>
      <div class="field">Enter Address</div>
      <div class="field">City And State</div>
      <div class="field">Phone Number</div>
      <div class="field">Date</div>
      <div class="submit">SUBMIT</div>
    </form>
  </div>
</section>

<section class="services-band">
  <div class="ghost" role="img" aria-label="Faded photo of a senior driver"></div>
  <h2>OUR SERVICES</h2>
  <p>Lorem Ipsum is simply dummy text of the printing and typesetting industry. Lorem Ipsum has been the industry's standard dummy text ever since the 1500s, when an unknown printer took a galley of type and scrambled it to make a type specimen book</p>
</section>

<section class="tiles">
  <div class="wrap">
    <div class="row">
      <div class="tile">
        <svg class="oct" viewBox="0 0 170 170"><polygon points="50,2 120,2 168,50 168,120 120,168 50,168 2,120 2,50" fill="#fff" stroke="#dcdcdc" stroke-width="2"/></svg>
        <div class="inner">
          <svg class="ico" viewBox="0 0 22 22"><path d="M4 20L9 2h4l5 18M11 5v3M11 11v3M11 17v3" stroke="#0c9b4c" stroke-width="2" fill="none"/></svg>
          <h4>LEARNING ROADS</h4>
          <p>Lorem Ipsum is simply dummy text of the printing and typesetting industry. Lorem Ipsum has been the industry</p>
        </div>
      </div>
      <div class="tile">
        <svg class="oct" viewBox="0 0 170 170"><polygon points="50,2 120,2 168,50 168,120 120,168 50,168 2,120 2,50" fill="#fff" stroke="#dcdcdc" stroke-width="2"/></svg>
        <div class="inner">
          <svg class="ico" viewBox="0 0 22 22"><path d="M11 4v16M6 9h10M3 13a8 8 0 0 0 16 0" stroke="#0c9b4c" stroke-width="2" fill="none"/><circle cx="11" cy="3" r="2" fill="#0c9b4c"/></svg>
          <h4>UNLIMITED CAR SUPPORT</h4>
          <p>Lorem Ipsum is simply dummy text of the printing and typesetting industry. Lorem Ipsum has been the industry</p>
        </div>
      </div>
      <div class="tile on">
        <svg class="oct" viewBox="0 0 170 170"><polygon points="50,2 120,2 168,50 168,120 120,168 50,168 2,120 2,50" fill="#0c9b4c" stroke="#fff" stroke-width="4"/></svg>
        <div class="inner">
          <svg class="ico" viewBox="0 0 22 22"><path d="M11 1l9 3v7c0 5-4 9-9 10C6 20 2 16 2 11V4z" fill="#fff"/></svg>
          <h4>DRIVING SCHOOL INSURES</h4>
          <p>Lorem Ipsum is simply dummy text of the printing and typesetting industry. Lorem Ipsum has been the industry</p>
        </div>
      </div>
      <div class="tile">
        <svg class="oct" viewBox="0 0 170 170"><polygon points="50,2 120,2 168,50 168,120 120,168 50,168 2,120 2,50" fill="#fff" stroke="#dcdcdc" stroke-width="2"/></svg>
        <div class="inner">
          <svg class="ico" viewBox="0 0 22 22"><rect x="3" y="2" width="16" height="18" rx="2" stroke="#0c9b4c" stroke-width="2" fill="none"/><path d="M6 6h10M6 11h3M11 11h3M6 15h3M11 15h3" stroke="#0c9b4c" stroke-width="2"/></svg>
          <h4>ANY TIME ANY LOCATION</h4>
          <p>Lorem Ipsum is simply dummy text of the printing and typesetting industry. Lorem Ipsum has been the industry</p>
        </div>
      </div>
    </div>
  </div>
</section>

<section class="participation">
  <div class="wrap">
    <h2>PARTICIPATION REQUIREMENTS</h2>
    <ul class="ticks">
      <li><svg viewBox="0 0 10 10"><path d="M1 5l3 3 5-7"/></svg>There is a one-time registration fee of $25.00 per participant.</li>
      <li><svg viewBox="0 0 10 10"><path d="M1 5l3 3 5-7"/></svg>A credit card is required for billing of individual trips.</li>
      <li><svg viewBox="0 0 10 10"><path d="M1 5l3 3 5-7"/></svg>We accommodate individuals with mobility needs including wheelchairs, walkers and service animals.</li>
      <li><svg viewBox="0 0 10 10"><path d="M1 5l3 3 5-7"/></svg>Drivers will not provide personal assistance like entering homes or escorting to an appointment.</li>
      <li><svg viewBox="0 0 10 10"><path d="M1 5l3 3 5-7"/></svg>Participants must have a valid phone and may request a companion program that offers travel support at no cost to those meeting qualification requirements.</li>
    </ul>
    <div class="part-photo" role="img" aria-label="Photo of a caregiver helping a senior man out of a car"></div>
  </div>
</section>

<section class="pricing">
  <div class="bg" role="img" aria-label="Dimmed background photo of parked cars"></div>
  <h2>YOUR PRICING PLAN</h2>
  <p class="lead">Lorem Ipsum is simply dummy text of the printing and typesetting industry. Lorem Ipsum has been the industry's standard dummy text ever since the 1500s, when an unknown printer took a galley of type and scrambled it to make a type specimen book</p>
  <div class="plans">
    <div class="plan">
      <div class="diamond"><span>$400</span></div>
      <h3>STANDARD</h3>
      <ul><li>3 Month Course</li><li>4 Hours Per Day</li><li>Weekly 2 Test</li><li>25 Video Classes</li><li>Driving Licence</li></ul>
      <div class="join">Join Now</div>
    </div>
    <div class="plan featured">
      <div class="diamond"><span>$300</span></div>
      <h3>BASIC</h3>
      <ul><li>3 Month Course</li><li>4 Hours Per Day</li><li>Weekly 2 Test</li><li>25 Video Classes</li><li>Driving Licence</li></ul>
      <div class="join">Join Now</div>
    </div>
    <div class="plan">
      <div class="diamond"><span>$250</span></div>
      <h3>UNLIMITED</h3>
      <ul><li>3 Month Course</li><li>4 Hours Per Day</li><li>Weekly 2 Test</li><li>25 Video Classes</li><li>Driving Licence</li></ul>
      <div class="join">Join Now</div>
    </div>
  </div>
</section>

<section class="testimonials">
  <h2>WHAT CLIENTS SAY</h2>
  <div class="avatar" role="img" aria-label="Client portrait"></div>
  <h4>MARISSA KELLAN</h4>
  <div class="role">Creative Head, Inc</div>
  <p class="quote"><span class="qm l">&ldquo;</span>Lorem Ipsum is simply dummy text of the printing and typesetting industry. Lorem Ipsum has been the industry's standard dummy text ever since the 1500s, when an unknown printer took a galley of type and scrambled it to make a type specimen book.<span class="qm r">&rdquo;</span></p>
  <span class="arrow prev"><svg viewBox="0 0 12 12"><path d="M8 1L3 6l5 5"/></svg></span>
  <span class="arrow next"><svg viewBox="0 0 12 12"><path d="M4 1l5 5-5 5"/></svg></span>
</section>

<section class="reservation">
  <h2>RESERVATION LINE</h2>
  <p>Please leave a message with your name and phone number if no one answers immediately.</p>
  <div class="phone">555-318-2046</div>
</section>

<section class="gowhen">
  <div class="wrap">
    <h2>GO WHEN AND WHERE YOU WANT TO GO WITH BRIGHT PATHWAYS</h2>
    <ul>
      <li><svg viewBox="0 0 10 10"><path d="M1 5l3 3 5-7"/></svg>Medical Appointment</li>
      <li><svg viewBox="0 0 10 10"><path d="M1 5l3 3 5-7"/></svg>Dental Appointment</li>
      <li><svg viewBox="0 0 10 10"><path d="M1 5l3 3 5-7"/></svg>Outpatient Testing And Procedures</li>
      <li><svg viewBox="0 0 10 10"><path d="M1 5l3 3 5-7"/></svg>Physical Therapy</li>
      <li><svg viewBox="0 0 10 10"><path d="M1 5l3 3 5-7"/></svg>Dialysis Clinic</li>
      <li><svg viewBox="0 0 10 10"><path d="M1 5l3 3 5-7"/></svg>Radiation Clinic</li>
      <li><svg viewBox="0 0 10 10"><path d="M1 5l3 3 5-7"/></svg>Church Events</li>
      <li><svg viewBox="0 0 10 10"><path d="M1 5l3 3 5-7"/></svg>Senior Centers/Adult Care Centers</li>
      <li><svg viewBox="0 0 10 10"><path d="M1 5l3 3 5-7"/></svg>Hospital/Nursing Home Discharge</li>
      <li><svg viewBox="0 0 10 10"><path d="M1 5l3 3 5-7"/></svg>Airport Transportation</li>
      <li><svg viewBox="0 0 10 10"><path d="M1 5l3 3 5-7"/></svg>Special Family Events</li>
      <li><svg viewBox="0 0 10 10"><path d="M1 5l3 3 5-7"/></svg>Grocery Shopping And Other Types Of Shopping</li>
      <li><svg viewBox="0 0 10 10"><path d="M1 5l3 3 5-7"/></svg>Bank And Post Office Errands</li>
      <li><svg viewBox="0 0 10 10"><path d="M1 5l3 3 5-7"/></svg>Barber/Beauty Shop Appointments</li>
    </ul>
    <div class="go-photo" role="img" aria-label="Photo of a caregiver buckling a senior woman into a car seat"></div>
  </div>
</section>

<section class="faq">
  <div class="wrap">
    <h2>FREQUENTLY ASKED QUESTIONS</h2>
    <p class="lead">Lorem Ipsum is simply dummy text of the printing and typesetting industry. Lorem Ipsum has been the industry's standard dummy text ever since the 1500s, when an unknown printer took a galley of type and scrambled it to make a type specimen book.</p>
    <div class="acc">
      <div class="item open">
        <div class="q"><svg viewBox="0 0 10 10"><path d="M1 5h8"/></svg>Lorem Ipsum is simply dummy text of the printing and typesetting industry ?</div>
        <div class="a">Lorem Ipsum is simply dummy text of the printing and typesetting industry. Lorem Ipsum has been the industry's standard dummy text ever since the 1500s, when an unknown printer took a galley of type and scrambled it to make a type specimen book.</div>
      </div>
      <div class="item"><div class="q"><svg viewBox="0 0 10 10"><path d="M1 5h8M5 1v8"/></svg>Lorem Ipsum is simply dummy text of the printing and typesetting industry ?</div></div>
      <div class="item"><div class="q"><svg viewBox="0 0 10 10"><path d="M1 5h8M5 1v8"/></svg>Lorem Ipsum is simply dummy text of the printing and typesetting industry ?</div></div>
      <div class="item"><div class="q"><svg viewBox="0 0 10 10"><path d="M1 5h8M5 1v8"/></svg>Lorem Ipsum is simply dummy text of the printing and typesetting industry ?</div></div>
      <div class="item"><div class="q"><svg viewBox="0 0 10 10"><path d="M1 5h8M5 1v8"/></svg>Lorem Ipsum is simply dummy text of the printing and typesetting industry ?</div></div>
    </div>
    <div class="car" role="img" aria-label="Photo of a red sports car"></div>
  </div>
</section>

<section class="newsletter">
  <div class="wrap">
    <div class="label"><small>NEWSLETTER FOR RECEIVE</small><strong>OUR LATEST COMPANYUPDATES</strong></div>
    <div class="field">Your Email
      <svg viewBox="0 0 12 12"><path d="M0 5L12 0 8 12 6 7z"/></svg>
    </div>
  </div>
</section>

<footer class="site-footer">
  <div class="cols">
    <div class="col">
      <h4>USEFUL LINKS</h4>
      <ul><li>Home</li><li>About Us</li><li>Services</li><li>Instructors</li><li>Blog</li><li>Contact Us</li></ul>
    </div>
    <div class="col">
      <h4>CONTACT US</h4>
      <p><b>Address :</b> 214 Meadowlark Lane, Suite 9, Fairview, CA 90210</p>
      <p><b>Phone Number :</b> 555-318-2046</p>
      <p><b>Email :</b> hello@brightpathways.org</p>
    </div>
    <div class="col">
      <h4>RECENT POSTS</h4>
      <div class="post"><i></i><span>Ninth Safety Drive<br>March 14, 2017</span></div>
      <div class="post"><i></i><span>Ninth Safety Drive<br>March 14, 2017</span></div>
    </div>
    <div class="col">
      <h4>RESERVATION PROCESS</h4>
      <p>Call ahead to schedule a ride at least one business day in advance.</p>
      <p>Reservations can be made seven days a week between the hours of 8 am and 5 pm.</p>
      <div class="rings"><i></i><i></i><i></i><i></i></div>
    </div>
  </div>
</footer>
<div class="copy">&copy; Copyright 2017 Bright Pathways. All Rights Reserved.</div>

</body>
</html>
```